Business Card for Coach - ready to print

Design Business Card ready to order prints www.lukasbrenner.coach

* An Overview / Background of the Business & Services
· Coaching
· Personal growth
* The Target Market / Audience you are trying to reach
· private person in different roles (self, familiy, business role)s
* Design Specifics; any preferences or ideas for Style, Colour, Imagery, etc
· See www.lukasbrenner.coach
· "simple" design
· (small) element of surprise / unusual element

* Information that will be placed in the Business Card
· Beratung und Coaching
· Address: Lukas Brenner, Talmatt 42, CH-8531 Seewil, Mobile +41 76 254 63 07
* Do you have an existing website or Facebook page where designers can learn more about your company?
· lukasbrenner.coach

Target Market(s)

private person in different roles (self, familiy, business role)

Industry/Entity Type

Life Coaching

Contact Information for Business Card

Lukas Brenner
Talmatt 42
CH-8531 Seewil

Mobile: +41 76 254 63 07
Email: lubr@sonnwelt.ch
www.lukasbrenner.coach

Font styles to use
Sans Serif

Colors

Designer to choose colors to be used in the design.

Requirements
Must have
• "simple" design
• element of surprise / unusual element
• Beratung & Coaching
• see www.lukasbrenner.coach for colors and so...
Nice to have
• TA Symbol (three rings on top of each other) - unsual presentation
• QR Code of Website (see if it fits in and still looks good).

```html
<!DOCTYPE html>
<html lang="de">
<head>
<meta charset="utf-8">
<title>Lukas Brenner – Visitenkarte</title>
<link rel="stylesheet" href="https://fonts.googleapis.com/css2?family=Roboto:wght@400;500&display=swap">
<style>
  :root {
    --page-bg: #c9c9c9;
    --front-blue: #94cbea;
    --front-green: #a6d2c4;
    --name-grey: #6a6a6a;
    --back-yellow: #f7b83b;
    --back-yellow-deep: #efae3a;
    --block-tan: #d9b27a;
    --block-edge: #c89c62;
    --white: #ffffff;
  }
  * { box-sizing: border-box; margin: 0; padding: 0; }
  html, body {
    width: 1200px; height: 1200px; overflow: hidden;
    background: var(--page-bg);
    font-family: "Roboto", Arial, sans-serif;
  }
  .stage { position: relative; width: 1200px; height: 1200px; }

  .card { position: absolute; left: 184px; width: 833px; height: 470px; overflow: hidden; }
  .card-front { top: 106px; }
  .card-back { top: 623px; height: 471px; }

  .card-texture { position: absolute; inset: 0; }
  .card-front .card-texture {
    background: linear-gradient(180deg, var(--front-blue) 0%, var(--front-green) 45%, var(--front-blue) 70%, var(--front-green) 100%);
  }
  .card-back .card-texture {
    background: linear-gradient(135deg, var(--back-yellow) 0%, var(--back-yellow) 60%, var(--back-yellow-deep) 100%);
  }

  .identity {
    position: absolute; left: 0; right: 0; top: 192px;
    text-align: center; color: var(--name-grey);
  }
  .identity-name {
    display: inline-block;
    font-weight: 500; font-size: 38px; line-height: 1;
    padding: 0 14px 5px;
    border-bottom: 2px solid var(--name-grey);
  }
  .identity-tagline {
    font-weight: 500; font-size: 27px; line-height: 1; margin-top: 6px;
  }

  .contact-list { position: absolute; left: 84px; top: 145px; list-style: none; }
  .contact-item { display: flex; align-items: center; height: 48px; }
  .contact-item:last-child { margin-top: 3px; }
  .contact-block {
    width: 52px; height: 46px; margin-right: 38px;
    background: var(--block-tan);
    border-right: 3px solid var(--block-edge);
    display: flex; align-items: center; justify-content: center;
  }
  .contact-block svg { width: 24px; height: 24px; }
  .contact-text {
    color: var(--white); font-size: 24px; letter-spacing: 1.5px; line-height: 1;
    white-space: nowrap;
  }
</style>
</head>
<body>
<main class="stage">
  <section class="card card-front">
    <div class="card-texture" role="img" aria-label="Soft blue and green photographic background of stacked wooden blocks"></div>
    <div class="identity">
      <h1 class="identity-name">Lukas Brenner</h1>
      <p class="identity-tagline">Beratung &amp; Coaching</p>
    </div>
  </section>

  <section class="card card-back">
    <div class="card-texture" role="img" aria-label="Warm yellow photographic background of wooden blocks"></div>
    <ul class="contact-list">
      <li class="contact-item">
        <span class="contact-block">
          <svg viewBox="0 0 24 24" fill="none" stroke="#fff" stroke-width="2" stroke-linejoin="round">
            <path d="M3 11 12 4l9 7"/><path d="M6 9.5V20h12V9.5"/>
            <circle cx="12" cy="13" r="2.2" fill="#fff" stroke="none"/>
          </svg>
        </span>
        <span class="contact-text">Talmatt 42, CH-8531 Seewil</span>
      </li>
      <li class="contact-item">
        <span class="contact-block">
          <svg viewBox="0 0 24 24" fill="#fff">
            <path d="M6.6 10.8a15 15 0 0 0 6.6 6.6l2.2-2.2a1 1 0 0 1 1-.25 11.4 11.4 0 0 0 3.6.57 1 1 0 0 1 1 1V20a1 1 0 0 1-1 1A17 17 0 0 1 3 4a1 1 0 0 1 1-1h3.5a1 1 0 0 1 1 1c0 1.25.2 2.45.57 3.57a1 1 0 0 1-.25 1z"/>
          </svg>
        </span>
        <span class="contact-text">+41 76 254 63 07</span>
      </li>
      <li class="contact-item">
        <span class="contact-block">
          <svg viewBox="0 0 24 24" fill="none" stroke="#fff" stroke-width="2" stroke-linejoin="round">
            <rect x="3" y="5" width="18" height="14" fill="#fff" stroke="none"/>
            <path d="M3 5l9 8 9-8" stroke="#d9b27a"/><path d="M3 19l7-6M21 19l-7-6" stroke="#d9b27a"/>
          </svg>
        </span>
        <span class="contact-text">lubr@sonnwelt.ch</span>
      </li>
      <li class="contact-item">
        <span class="contact-block">
          <svg viewBox="0 0 24 24" fill="none" stroke="#fff" stroke-width="1.8">
            <circle cx="12" cy="12" r="9"/><path d="M3 12h18M12 3c3 3 3 15 0 18M12 3c-3 3-3 15 0 18"/>
          </svg>
        </span>
        <span class="contact-text">www.lukasbrenner.coach</span>
      </li>
    </ul>
  </section>
</main>
</body>
</html>
```